NurseLeaf Baby wet wipes with Chamomile 100 pcs

I would like a modern, unisex baby wipe packaging design. I would like pastel colors that are neutral and trendy. The packaging should feature nature-inspired patterns that are subtle, clean, and timelessly adorable.

Target Market(s)

family

Industry/Entity Type

Baby Products - Personal Care

Colors
0094D4
00A9DD
6FCCEA
C7EBF8
E9F6FB
00AB8E
00BBA5
67D7C9
C6EFE9
E9F9F6
59FF00
82FF00
B8FF75
E3FFCB
F4FFEA
FFF300
FFF600
FEFA6F
FFFEC7
FFFEE8
FFC000
F8CF3A
FAE287
FDF2CF
FEFAEE

Requirements
Must have
• For our purposes we need the final artwork to be provided in a true vector format such as AI, EPS, or vector based PDF
Nice to have
• The product is dermatologically tested

```html
<!DOCTYPE html>
<html lang="en">
<head>
<meta charset="utf-8">
<title>NurseLeaf Baby Wet Wipes with Chamomile – Pack Front</title>
<link href="https://fonts.googleapis.com/css2?family=Montserrat:wght@500;600;800&family=Sniglet:wght@400;800&display=swap" rel="stylesheet">
<style>
  :root{
    --canvas:#eef1f3;
    --pack-white:#fbfdfe;
    --band-blue:#5cbfd9;
    --band-blue-dark:#4aaecb;
    --crimp:#e3f1f7;
    --navy:#1f4fa3;
    --teal:#4dbfa6;
    --teal-pill:#5cc3b1;
    --blush:#f4b6aa;
    --coral:#e8a092;
    --skin-a:#f3d2bf;
    --skin-b:#d9a48c;
    --white:#ffffff;
  }
  *{margin:0;padding:0;box-sizing:border-box}
  html,body{width:1200px;height:800px;overflow:hidden;background:var(--canvas)}
  .canvas{position:relative;width:1200px;height:800px;font-family:"Montserrat",sans-serif}
  .pack-shape{position:absolute;left:0;top:0}
  .crimp{position:absolute;top:120px;width:40px;height:560px;
    background:repeating-linear-gradient(90deg,rgba(255,255,255,.55) 0 2px,rgba(180,215,228,.35) 2px 5px)}
  .crimp--left{left:60px;border-radius:10px 0 0 10px}
  .crimp--right{left:1100px;border-radius:0 10px 10px 0}

  .claim-pill{position:absolute;left:285px;top:205px;background:var(--teal-pill);color:var(--white);
    font-weight:500;font-size:16px;padding:6px 16px;border-radius:18px}
  .brand-name{position:absolute;left:280px;top:240px;color:var(--navy);font-weight:800;font-size:88px;letter-spacing:1px;line-height:1}
  .product-name{position:absolute;left:420px;top:345px;color:var(--teal);font-family:"Sniglet",sans-serif;font-weight:800;font-size:56px;line-height:1}
  .product-variant{position:absolute;left:560px;top:410px;color:var(--navy);font-weight:600;font-size:26px}

  .count-badge{position:absolute;left:820px;top:145px;width:120px;height:120px;border-radius:50%;background:var(--blush);
    color:var(--white);display:flex;flex-direction:column;align-items:center;justify-content:center;font-weight:600;line-height:1}
  .count-badge__num{font-size:40px}
  .count-badge__unit{font-size:30px}

  .seal{position:absolute;width:108px;height:108px;border-radius:50%;background:var(--navy);
    display:flex;align-items:center;justify-content:center}
  .seal__inner{width:72px;height:72px;border-radius:50%;background:var(--white);display:flex;align-items:center;justify-content:center}
  .seal__dot{width:34px;height:34px;border-radius:50%;background:var(--coral)}
  .seal--one{left:955px;top:190px}
  .seal--two{left:985px;top:318px}

  .baby-photo{position:absolute;left:150px;top:440px;width:240px;height:120px;border-radius:60px 40px 20px 60px;
    background:radial-gradient(ellipse at 30% 45%,var(--skin-a),var(--skin-b))}

  .benefits{position:absolute;left:120px;top:568px;display:flex}
  .benefit{width:150px;display:flex;flex-direction:column;align-items:center;color:var(--white);
    font-size:14px;font-weight:500;text-align:center;line-height:1.2;border-right:1px solid rgba(255,255,255,.45)}
  .benefit:last-child{border-right:none}
  .benefit__icon{width:46px;height:46px;border-radius:50%;background:var(--white);margin-bottom:6px;
    display:flex;align-items:center;justify-content:center}

  .water-claim{position:absolute;left:770px;top:465px;width:170px;height:125px;border-radius:18px 18px 0 0;background:var(--coral);
    color:var(--white);display:flex;flex-direction:column;align-items:center;justify-content:center;line-height:1.05}
  .water-claim__lead{font-size:15px;font-weight:600}
  .water-claim__value{font-size:50px;font-weight:800}
  .water-claim__tail{font-size:15px;font-weight:600}
</style>
</head>
<body>
<main class="canvas">
  <svg class="pack-shape" width="1200" height="800" viewBox="0 0 1200 800" aria-hidden="true">
    <defs>
      <clipPath id="pack-clip"><rect x="60" y="120" width="1080" height="560" rx="12"/></clipPath>
    </defs>
    <g clip-path="url(#pack-clip)">
      <rect x="60" y="120" width="1080" height="560" fill="var(--pack-white)"/>
      <path d="M60,560 C320,540 560,500 760,420 C930,350 1020,250 1070,120 L1140,120 L1140,680 L60,680 Z" fill="var(--band-blue)"/>
      <path d="M1070,120 C1020,250 930,350 760,420 L770,425 C950,355 1040,255 1090,120 Z" fill="var(--band-blue-dark)" opacity=".5"/>
    </g>
  </svg>
  <div class="crimp crimp--left"></div>
  <div class="crimp crimp--right"></div>

  <span class="claim-pill">Antibacterial</span>
  <h1 class="brand-name">NurseLeaf</h1>
  <p class="product-name">Baby Wet Wipes</p>
  <p class="product-variant">with Chamomile</p>

  <div class="count-badge"><span class="count-badge__num">100</span><span class="count-badge__unit">pcs</span></div>

  <div class="seal seal--one"><div class="seal__inner"><div class="seal__dot"></div></div></div>
  <div class="seal seal--two"><div class="seal__inner"><div class="seal__dot"></div></div></div>

  <div class="baby-photo" role="img" aria-label="Photo of a sleeping newborn baby resting on its hands"></div>

  <ul class="benefits">
    <li class="benefit">
      <span class="benefit__icon"><svg width="26" height="26" viewBox="0 0 26 26"><path d="M13 22 V12 M13 14 C8 14 5 10 5 5 C10 5 13 8 13 14 M13 14 C18 14 21 10 21 5 C16 5 13 8 13 14" fill="none" stroke="var(--band-blue)" stroke-width="2" stroke-linecap="round"/></svg></span>
      Pure &amp; Natural<br>ingredients
    </li>
    <li class="benefit">
      <span class="benefit__icon"><svg width="26" height="26" viewBox="0 0 26 26"><path d="M6 21 L18 7 M18 4 C22 8 20 15 10 18 C9 12 12 6 18 4 Z" fill="none" stroke="var(--band-blue)" stroke-width="2" stroke-linejoin="round"/></svg></span>
      Ultra soft &amp;<br>extra strong
    </li>
    <li class="benefit">
      <span class="benefit__icon"><svg width="26" height="26" viewBox="0 0 26 26"><rect x="8" y="10" width="10" height="12" rx="2" fill="none" stroke="var(--band-blue)" stroke-width="2"/><rect x="10" y="5" width="6" height="5" fill="var(--band-blue)"/><circle cx="6" cy="5" r="1.2" fill="var(--band-blue)"/><circle cx="4" cy="8" r="1.2" fill="var(--band-blue)"/></svg></span>
      Fragrance<br>Free
    </li>
    <li class="benefit">
      <span class="benefit__icon"><svg width="26" height="26" viewBox="0 0 26 26"><path d="M4 17 C8 15 11 16 14 18 L20 15 C22 14 23 16 21 17 L14 21 L4 21 Z" fill="none" stroke="var(--band-blue)" stroke-width="2" stroke-linejoin="round"/><path d="M13 12 C10 9 9 7 11 5.5 C12.5 4.5 13 6 13 6 C13 6 13.5 4.5 15 5.5 C17 7 16 9 13 12 Z" fill="var(--band-blue)"/></svg></span>
      Sensitive<br>Skin
    </li>
  </ul>

  <div class="water-claim">
    <span class="water-claim__lead">Made with</span>
    <span class="water-claim__value">99%</span>
    <span class="water-claim__tail">purified water</span>
  </div>
</main>
</body>
</html>
```